Velvet Pressings Techno Label Business Card

I'm looking for a very clean business card for my Velvet Pressings music label. The label focusses on techno music. The card should include:

• my name : Bram Quintel as "Founder & CEO"
• email address: bram@velvet-pressings.example
• web: www.velvet-pressings.example
• facebook logo + /velvetpress
• twitter logo + /velvetpress
• soundcloud logo + /velvetpressings

Feel free to include your ideas! I'm looking forward to discuss about it.

Bram

Industry/Entity Type

Business

Contact Information for Business Card

I don't like glossy cards. Prefer matt.

Requirements
Nice to have
• Maybe on one side the complete logo, other side just the icon.
Should not have
• Flashy stuff. Must be clean and business like style.

```html
<!DOCTYPE html>
<html lang="en">
<head>
<meta charset="utf-8">
<title>Velvet Pressings — Business Card</title>
<link rel="stylesheet" href="https://fonts.googleapis.com/css2?family=Jura:wght@500;600&family=Cinzel:wght@700&family=Quicksand:wght@500;700&family=Comfortaa:wght@500&display=swap">
<style>
  :root {
    --backdrop: #2b2b2b;
    --card-white: #ffffff;
    --card-dark: #4a4a4a;
    --brand-orange: #ef6a21;
    --title-grey: #6f6f6f;
    --ink: #1e1e1e;
  }
  * { box-sizing: border-box; margin: 0; padding: 0; }
  html, body {
    width: 1200px; height: 1171px; overflow: hidden;
    background: var(--backdrop);
  }
  .canvas { position: relative; width: 1200px; height: 1171px; }

  .card {
    position: absolute;
    width: 710px; height: 410px;
    overflow: hidden;
  }
  .card--front { left: 90px; top: 130px; background: var(--card-white); }
  .card--back  { left: 400px; top: 620px; background: var(--card-dark); }

  .stripe { position: absolute; top: 0; bottom: 0; background: var(--brand-orange); }
  .card--front .stripe--outer-left  { left: 22px;  width: 18px; }
  .card--front .stripe--inner-left  { left: 48px;  width: 5px; }
  .card--front .stripe--inner-right { right: 48px; width: 5px; }
  .card--front .stripe--outer-right { right: 22px; width: 18px; }
  .card--back .stripe--outer-left  { left: 30px;  width: 5px; }
  .card--back .stripe--inner-left  { left: 43px;  width: 18px; }
  .card--back .stripe--inner-right { right: 43px; width: 18px; }
  .card--back .stripe--outer-right { right: 30px; width: 5px; }

  .brand {
    position: absolute; left: 72px; top: 30px;
    display: flex; align-items: center; gap: 10px;
  }
  .brand__dot {
    width: 30px; height: 30px; border-radius: 50%;
    background: var(--brand-orange);
  }
  .brand__name {
    font-family: "Quicksand", sans-serif; font-weight: 700;
    font-size: 25px; color: var(--brand-orange);
  }

  .identity {
    position: absolute; left: 0; right: 0; top: 138px;
    text-align: center;
  }
  .identity__name {
    font-family: "Jura", sans-serif; font-weight: 600;
    font-size: 38px; letter-spacing: 3px; text-transform: uppercase;
    color: var(--brand-orange); line-height: 1;
  }
  .identity__initial { font-size: 50px; }
  .identity__role {
    margin-top: 6px;
    font-family: "Cinzel", serif; font-weight: 700;
    font-size: 28px; letter-spacing: 2px;
    color: var(--title-grey);
  }

  .social {
    position: absolute; left: 72px; right: 72px; top: 292px;
    display: flex; justify-content: center; gap: 34px;
    font-family: "Comfortaa", sans-serif; font-weight: 500;
    font-size: 15px; color: var(--ink);
  }
  .social__item { display: flex; align-items: center; gap: 8px; }
  .social__dot {
    width: 18px; height: 18px; border-radius: 50%;
    background: var(--brand-orange);
  }

  .contact {
    position: absolute; left: 72px; right: 72px; bottom: 24px;
    display: flex; justify-content: space-between;
    font-family: "Comfortaa", sans-serif; font-weight: 500;
    font-size: 15px; color: var(--ink);
  }

  .back-mark {
    position: absolute; inset: 0;
    display: flex; align-items: center; justify-content: center; gap: 16px;
  }
  .back-mark__dot {
    width: 54px; height: 54px; border-radius: 50%;
    background: var(--brand-orange);
  }
  .back-mark__name {
    font-family: "Quicksand", sans-serif; font-weight: 700;
    font-size: 44px; color: var(--brand-orange);
  }
</style>
</head>
<body>
<main class="canvas">
  <section class="card card--front" aria-label="Business card front">
    <span class="stripe stripe--outer-left"></span>
    <span class="stripe stripe--inner-left"></span>
    <span class="stripe stripe--inner-right"></span>
    <span class="stripe stripe--outer-right"></span>

    <div class="brand">
      <span class="brand__dot"></span>
      <span class="brand__name">Velvet Pressings</span>
    </div>

    <div class="identity">
      <h1 class="identity__name"><span class="identity__initial">B</span>ram <span class="identity__initial">Q</span>uintel</h1>
      <p class="identity__role">Founder &amp; CEO</p>
    </div>

    <ul class="social" aria-label="Social profiles">
      <li class="social__item"><span class="social__dot"></span><span class="social__handle">/velvetpress</span></li>
      <li class="social__item"><span class="social__dot"></span><span class="social__handle">/velvetpress</span></li>
      <li class="social__item"><span class="social__dot"></span><span class="social__handle">/velvetpressings</span></li>
    </ul>

    <div class="contact">
      <span class="contact__email">bram@velvet-pressings.example</span>
      <span class="contact__web">www.velvet-pressings.example</span>
    </div>
  </section>

  <section class="card card--back" aria-label="Business card back">
    <span class="stripe stripe--outer-left"></span>
    <span class="stripe stripe--inner-left"></span>
    <span class="stripe stripe--inner-right"></span>
    <span class="stripe stripe--outer-right"></span>

    <div class="back-mark">
      <span class="back-mark__dot"></span>
      <span class="back-mark__name">Velvet Pressings</span>
    </div>
  </section>
</main>
</body>
</html>
```